Birch Flooring Supply

Basic one-sided business card design using the attached logo. Vintage americana theme. Font is modified Arial Nova Cond, but anything that coordinates can be used

```html
<!DOCTYPE html>
<html lang="en">
<head>
<meta charset="utf-8">
<title>Birch Flooring Supply — Business Card</title>
<link href="https://fonts.googleapis.com/css2?family=Montserrat:wght@400;500;700&display=swap" rel="stylesheet">
<style>
  :root {
    --backdrop: #b3b3b3;
    --card: #0a0a0a;
    --tan: #bc9469;
    --white: #ffffff;
  }
  * { margin: 0; padding: 0; box-sizing: border-box; }
  html, body {
    width: 1200px; height: 900px; overflow: hidden;
    background: var(--backdrop);
    font-family: "Montserrat", Arial, sans-serif;
  }
  .card {
    position: absolute;
    left: 100px; top: 165px;
    width: 1000px; height: 570px;
    background: var(--card);
    border-radius: 26px;
    overflow: hidden;
  }
  .band { position: absolute; background: var(--tan); width: 46px; }
  .band--left { left: 30px; top: 255px; height: 285px; }
  .band--right { right: 30px; top: 75px; height: 255px; }

  .brand {
    position: absolute;
    left: 215px; top: 190px;
    width: 290px; height: 290px;
    display: flex; align-items: center; justify-content: center;
  }
  .brand__ring {
    position: absolute; inset: 0;
    border: 4px solid var(--tan);
    border-radius: 50%;
  }
  .brand__name {
    position: relative;
    color: var(--white);
    font-weight: 700;
    font-size: 30px;
    line-height: 1.15;
    text-align: center;
    letter-spacing: 1px;
    text-transform: uppercase;
  }

  .divider {
    position: absolute;
    left: 530px; top: 215px;
    width: 2px; height: 250px;
    background: var(--tan);
  }
  .contact {
    position: absolute;
    left: 565px; top: 200px;
    color: var(--white);
  }
  .contact__name {
    color: var(--tan);
    font-weight: 700;
    font-size: 34px;
    line-height: 1.1;
  }
  .contact__role { font-size: 20px; margin-top: 2px; }
  .contact__address { font-size: 20px; line-height: 1.25; margin-top: 30px; }
  .contact__list { list-style: none; margin-top: 14px; }
  .contact__item {
    display: flex; align-items: center; gap: 14px;
    font-size: 20px; line-height: 1.6;
  }
  .contact__item--plain { padding-left: 0; }
  .icon { width: 18px; height: 18px; fill: var(--tan); flex: none; }
</style>
</head>
<body>
  <div class="card">
    <div class="band band--left"></div>
    <div class="band band--right"></div>

    <div class="brand">
      <div class="brand__ring"></div>
      <div class="brand__name">Birch<br>Flooring<br>Supply</div>
    </div>

    <div class="divider"></div>

    <div class="contact">
      <div class="contact__name">Daniel Hayes</div>
      <div class="contact__role">Managing Director</div>
      <div class="contact__address">418 Linden Ave, #112<br>Fairview, OH 430157</div>
      <ul class="contact__list">
        <li class="contact__item">
          <svg class="icon" viewBox="0 0 24 24" aria-hidden="true"><path d="M6.6 10.8a15.1 15.1 0 0 0 6.6 6.6l2.2-2.2a1 1 0 0 1 1-.25 11.4 11.4 0 0 0 3.6.57 1 1 0 0 1 1 1V20a1 1 0 0 1-1 1A17 17 0 0 1 3 4a1 1 0 0 1 1-1h3.5a1 1 0 0 1 1 1c0 1.25.2 2.45.57 3.57a1 1 0 0 1-.25 1z"/></svg>
          555-318-0427
        </li>
        <li class="contact__item">
          <svg class="icon" viewBox="0 0 24 24" aria-hidden="true"><path d="M2 5h20v14H2z M3.5 6.5 12 13l8.5-6.5" fill="none" stroke="#bc9469" stroke-width="2"/><path d="M2 6l10 7.5L22 6v13H2z"/></svg>
          info@birchflooring.com
        </li>
        <li class="contact__item">
          <svg class="icon" viewBox="0 0 24 24" aria-hidden="true"><circle cx="12" cy="12" r="10"/><path d="M2 12h20M12 2c3 3 3 17 0 20M12 2c-3 3-3 17 0 20" fill="none" stroke="#0a0a0a" stroke-width="1.6"/></svg>
          www.birchflooring.com
        </li>
      </ul>
    </div>
  </div>
</body>
</html>
```